Banner Ads for LED Grow Lights

Title - Banner Ads needed for Horticultural Lighting Technology sites

BrevoGlow LED is a technology firm that develops and sells LED Grow Lights for greenhouse growers, sustainable foods, urban gardening, off-grid growing, and cannabis growers.

Our clientele includes large scale farms, universities, schools, research labs, small and large cannabis growers,as well as individual home gardeners.

Our products are energy efficient, earth-friendly, and allow gardeners to grow fresh, clean, healthy food or medicinals all year round INDOORS. No sunlight required. Also used as supplemental lighting for outdoor greenhouses to boost productivity.

Competitors:
Fernquarryled.com
Kelvantatrading.com
842tovled.com
plandiva.com

I am looking for two sets of banner ads with the following sizes:
970x90
728x90 - gif
160x600 - gif
300x250

One set will be for the food growers and one set targeting cannabis growers.

Colors are very important - I want crisp, vibrant colors as found in nature . . . think grass, sky, apples, tomatoes, fresh greens, peppers, etc. Incorporated images must look so good people would want to lick their computer screen.

Due to the nature of the product, we do attract growers of cannabis. We embrace cannabis growers but I do not want the banners to look like they are for some head shop. I am looking for more of a friendly feel to elevate cannabis out of the negative - cannabis imagery is welcome but must be natural and professional

Feel free to use images from our site - BrevoGlowLED.com and our logo is attached.

Requirements
Must have
• Use the word cannabis when needed, not marijuana or any other slang term.

```html
<!DOCTYPE html>
<html lang="en">
<head>
<meta charset="utf-8">
<title>BrevoGlow LED – Banner Set</title>
<link rel="stylesheet" href="https://fonts.googleapis.com/css2?family=Arimo:wght@400;700&display=swap">
<style>
  :root {
    --page: #ffffff;
    --frame: #8a8a8a;
    --ink: #555555;
    --ink-dark: #333333;
    --magenta: #e619c8;
    --magenta-soft: #f7a8ec;
    --panel-top: #ffffff;
    --panel-bottom: #e4e4e4;
    --green-light: #9ad43a;
    --green-mid: #6cb52a;
    --green-dark: #3f8a1c;
    --button-ring: #2e5a12;
    --photo-top: #eef1f2;
    --photo-sky: #9cc3d3;
    --photo-leaf: #86a94f;
    --photo-crate: #c39063;
  }
  * { box-sizing: border-box; margin: 0; padding: 0; }
  html, body {
    width: 1200px; height: 1200px; overflow: hidden;
    background: var(--page);
    font-family: "Arimo", Arial, sans-serif;
  }
  .sheet {
    position: absolute; left: 0; top: 0;
    width: 850px; height: 850px;
    transform: scale(1.41176); transform-origin: 0 0;
  }
  .banner {
    position: absolute; overflow: hidden;
    border: 1px solid var(--frame);
    background: linear-gradient(var(--panel-top), var(--panel-bottom));
  }
  .headline { font-weight: 700; color: var(--ink); text-align: center; line-height: 1; }
  .tagline, .body-copy { color: var(--ink); text-align: center; line-height: 1; }
  .photo {
    position: absolute;
    background: linear-gradient(180deg, var(--photo-top) 0%, var(--photo-sky) 40%, var(--photo-leaf) 72%, var(--photo-crate) 100%);
  }
  .swoosh { position: absolute; }
  .brand {
    position: absolute; color: var(--ink); font-weight: 400;
    white-space: nowrap; text-align: center;
  }
  .cta {
    position: absolute; height: 35px; width: 142px;
    border-radius: 4px;
    background: linear-gradient(var(--green-light), var(--green-mid) 55%, var(--green-dark));
    border: 1px solid var(--green-dark);
    color: #fff; font-weight: 700; font-size: 16px;
    display: flex; align-items: center; padding-left: 11px;
  }
  .cta svg { position: absolute; right: 6px; top: 4px; }
  .size-label { position: absolute; font-size: 16px; color: var(--ink-dark); white-space: nowrap; }
  .size-label .weight { color: var(--magenta); margin-left: 6px; }

  /* Leaderboard */
  .leaderboard { left: 60px; top: 30px; width: 728px; height: 90px; }
  .leaderboard .copy { position: absolute; left: 0; top: 6px; width: 300px; }
  .leaderboard .headline { font-size: 19px; }
  .leaderboard .tagline { font-size: 17px; margin-top: 2px; }
  .leaderboard .body-copy { font-size: 14px; margin-top: 2px; line-height: 1.08; }
  .leaderboard .photo { left: 305px; top: 0; width: 246px; height: 90px; }
  .leaderboard .brand { left: 552px; top: 8px; width: 175px; font-size: 17px; }
  .leaderboard .cta { left: 569px; top: 43px; }

  /* Medium rectangle */
  .rectangle { left: 62px; top: 243px; width: 300px; height: 250px; }
  .rectangle .copy { position: absolute; left: 0; top: 4px; width: 300px; }
  .rectangle .headline { font-size: 19px; }
  .rectangle .tagline { font-size: 17px; margin-top: 2px; }
  .rectangle .body-copy { font-size: 14px; margin-top: 2px; line-height: 1.08; }
  .rectangle .photo { left: 0; top: 96px; width: 300px; height: 96px; }
  .rectangle .brand { left: 8px; top: 212px; width: 118px; font-size: 14px; }
  .rectangle .cta { left: 131px; top: 202px; }

  /* Skyscraper */
  .skyscraper { left: 630px; top: 182px; width: 160px; height: 600px; }
  .skyscraper .copy { position: absolute; left: 0; top: 6px; width: 160px; }
  .skyscraper .headline { font-size: 20px; }
  .skyscraper .tagline { font-size: 17px; margin-top: 11px; line-height: 1.15; }
  .skyscraper .body-copy { font-size: 16px; margin-top: 9px; line-height: 1.18; }
  .skyscraper .photo { left: 0; top: 246px; width: 160px; height: 250px; }
  .skyscraper .brand { left: 0; top: 508px; width: 160px; font-size: 17px; }
  .skyscraper .cta { left: 7px; top: 553px; }
</style>
</head>
<body>
<main class="sheet">

  <section class="banner leaderboard" aria-label="728 by 90 banner">
    <div class="copy">
      <h1 class="headline">LED GROW LIGHTS</h1>
      <p class="tagline">Technology in Sync With nature.</p>
      <p class="body-copy">Experience the next generation of<br>hortikultura lighting.</p>
    </div>
    <div class="photo" role="img" aria-label="Photo: LED grow light fixture above a person holding a crate of fresh vegetables, with strawberries and cannabis leaves"></div>
    <svg class="swoosh" style="left:285px;top:0" width="30" height="90" viewBox="0 0 30 90">
      <defs><linearGradient id="lbFade" x1="0" y1="0" x2="0" y2="1"><stop offset="0" stop-color="#fff"/><stop offset="1" stop-color="#e4e4e4"/></linearGradient></defs>
      <path d="M0 0 H12 Q26 45 12 90 H0 Z" fill="url(#lbFade)"/>
      <path d="M12 0 Q26 45 12 90 L20 90 Q34 45 20 0 Z" fill="var(--magenta)"/>
    </svg>
    <div class="brand">BrevoGlow LED</div>
    <div class="cta">More Info!
      <svg width="26" height="26" viewBox="0 0 26 26"><circle cx="13" cy="13" r="12" fill="#f4f4f4"/><circle cx="13" cy="13" r="10.5" fill="var(--button-ring)"/><path d="M10 7 L19 13 L10 19 Z" fill="#eef6e4"/></svg>
    </div>
  </section>
  <div class="size-label" style="left:331px;top:132px">728X90<span class="weight">23.0Kb</span></div>

  <section class="banner rectangle" aria-label="300 by 250 banner">
    <div class="copy">
      <h2 class="headline">LED GROW LIGHTS</h2>
      <p class="tagline">Technology in Sync With nature.</p>
      <p class="body-copy">Experience the next generation of<br>hortikultura lighting.</p>
    </div>
    <div class="photo" role="img" aria-label="Photo: LED grow light fixture over a crate of fresh vegetables, strawberries and a cannabis plant"></div>
    <svg class="swoosh" style="left:0;top:79px" width="300" height="20" viewBox="0 0 300 20">
      <path d="M0 4 Q150 -4 300 6 L300 17 L0 17 Z" fill="var(--magenta)"/>
      <path d="M0 10 Q150 2 300 12 L300 20 L0 20 Z" fill="var(--magenta-soft)"/>
    </svg>
    <div class="brand">BrevoGlow LED</div>
    <div class="cta">More Info!
      <svg width="26" height="26" viewBox="0 0 26 26"><circle cx="13" cy="13" r="12" fill="#f4f4f4"/><circle cx="13" cy="13" r="10.5" fill="var(--button-ring)"/><path d="M10 7 L19 13 L10 19 Z" fill="#eef6e4"/></svg>
    </div>
  </section>
  <div class="size-label" style="left:125px;top:503px">300X250<span class="weight">27.8Kb</span></div>

  <section class="banner skyscraper" aria-label="160 by 600 banner">
    <div class="copy">
      <h3 class="headline">LED GROW<br>LIGHTS</h3>
      <p class="tagline">Technology<br>in Sync<br>With nature.</p>
      <p class="body-copy">Experience<br>the next<br>generation of<br>hortikultura<br>lighting.</p>
    </div>
    <div class="photo" role="img" aria-label="Photo: LED grow light fixture above a person in a blue shirt holding a crate of fresh vegetables"></div>
    <svg class="swoosh" style="left:0;top:227px" width="160" height="22" viewBox="0 0 160 22">
      <path d="M0 6 Q80 -4 160 8 L160 18 L0 18 Z" fill="var(--magenta)"/>
      <path d="M0 12 Q80 4 160 14 L160 22 L0 22 Z" fill="var(--magenta-soft)"/>
    </svg>
    <div class="brand">BrevoGlow LED</div>
    <div class="cta">More Info!
      <svg width="26" height="26" viewBox="0 0 26 26"><circle cx="13" cy="13" r="12" fill="#f4f4f4"/><circle cx="13" cy="13" r="10.5" fill="var(--button-ring)"/><path d="M10 7 L19 13 L10 19 Z" fill="#eef6e4"/></svg>
    </div>
  </section>
  <div class="size-label" style="left:630px;top:791px">160X600<span class="weight">30.4Kb</span></div>

</main>
</body>
</html>
```